Summit Guest Partners

An Editable Business Card Template For SGP & SGH
Similar or Different Design

418 W. Marlow Ridge Pkwy.
Suite 2230
Irving, TX 75038

```html
<!DOCTYPE html>
<html lang="en">
<head>
<meta charset="utf-8">
<title>Summit Guest Partners – Business Cards</title>
<link href="https://fonts.googleapis.com/css2?family=Lato:wght@400;700&family=Roboto+Slab:wght@700&display=swap" rel="stylesheet">
<style>
:root{
  --backdrop:#8f8f8f;
  --card:#ffffff;
  --brand-red:#8c181b;
  --ink:#1a1a1a;
  --body:#3a3a3a;
  --muted:#555555;
}
*{margin:0;padding:0;box-sizing:border-box}
html,body{width:1200px;height:1200px;overflow:hidden;background:var(--backdrop)}
.canvas{position:relative;width:1200px;height:1200px}
.card{position:absolute;left:269px;width:663px;height:380px;background:var(--card);box-shadow:0 3px 6px rgba(0,0,0,.35)}
.card--front{top:180px}
.card--back{top:630px}
.card__band{position:absolute;left:0;bottom:0;width:100%;height:54px;background:var(--brand-red);color:#fff;
  font:700 28px/54px "Roboto Slab",serif;text-align:center}
.abs{position:absolute;white-space:nowrap}
.brand{display:flex;align-items:center;gap:10px}
.brand__dot{width:22px;height:22px;border-radius:50%;background:var(--brand-red);flex:none}
.brand__name{font:700 20px/1.15 "Roboto Slab",serif;color:var(--brand-red)}
.person__name{font:700 30px/1 "Roboto Slab",serif;color:var(--ink)}
.person__title{font:400 19px/1 "Lato",sans-serif;color:var(--brand-red)}
.address{font:400 17px/22.5px "Lato",sans-serif;color:var(--body)}
.contact{list-style:none;font-family:"Lato",sans-serif;color:var(--body)}
.contact li{display:flex;align-items:center;gap:10px}
.contact .big{font-size:22px;line-height:27px}
.contact .small{font-size:17px;line-height:21px}
.contact svg{width:14px;height:14px;fill:var(--brand-red);flex:none}
.accent{color:var(--brand-red);font-weight:700}
.office{text-align:center;width:300px}
.office__label{font:700 19px/1 "Roboto Slab",serif;color:var(--ink);letter-spacing:.3px}
.office__phone{font:700 35px/1 "Roboto Slab",serif;color:var(--brand-red);margin-top:6px}
.office__address{font:400 12px/1 "Lato",sans-serif;color:var(--body);margin-top:6px}
.pitch{font:700 26px/26px "Roboto Slab",serif;color:var(--brand-red)}
.features{list-style:none;font:400 16px/26px "Lato",sans-serif;color:var(--muted)}
.features li{display:flex;align-items:center;gap:10px}
.features svg{width:22px;height:12px;flex:none}
</style>
</head>
<body>
<main class="canvas">

  <section class="card card--front">
    <div class="abs brand" style="left:50px;top:156px">
      <span class="brand__dot"></span>
      <span class="brand__name">SGH<br>Summit Guest<br>Housing</span>
    </div>

    <div class="abs person__name" style="left:359px;top:38px">Dana Whitfield</div>
    <div class="abs person__title" style="left:357px;top:78px">Sales Manager</div>

    <div class="abs address" style="left:358px;top:107px">
      418 W. Marlow Ridge Pkwy.<br>Suite 2230<br>Irving, TX 75038
    </div>

    <ul class="abs contact" style="left:358px;top:178px">
      <li class="big"><svg viewBox="0 0 24 24"><path d="M6.6 10.8a15 15 0 0 0 6.6 6.6l2.2-2.2c.3-.3.7-.4 1-.2 1.1.4 2.3.6 3.6.6.6 0 1 .4 1 1V20c0 .6-.4 1-1 1A17 17 0 0 1 3 4c0-.6.4-1 1-1h3.5c.6 0 1 .4 1 1 0 1.3.2 2.5.6 3.6.1.3 0 .7-.2 1z"/></svg>214-555-0147</li>
      <li class="big"><svg viewBox="0 0 24 24"><path d="M7 1h10a2 2 0 0 1 2 2v18a2 2 0 0 1-2 2H7a2 2 0 0 1-2-2V3a2 2 0 0 1 2-2zm0 3v14h10V4zm5 15.5a1 1 0 1 0 0 2 1 1 0 0 0 0-2z"/></svg>480-555-0192</li>
      <li class="small"><svg viewBox="0 0 24 24"><path d="M2 5h20v14H2zm2 2v.4l8 5.2 8-5.2V7zm0 2.8V17h16V9.8l-8 5.2z"/></svg>DWhitfield@summitguest.com</li>
      <li class="small"><svg viewBox="0 0 24 24"><circle cx="12" cy="12" r="10"/></svg>www.<span class="accent">SGPOilField</span>.com</li>
    </ul>

    <div class="card__band">Oil Field Housing on Autopilot</div>
  </section>

  <section class="card card--back">
    <div class="abs brand" style="left:88px;top:52px">
      <span class="brand__dot"></span>
      <span class="brand__name">SGP<br>Summit Guest<br>Partners</span>
    </div>

    <div class="abs office" style="left:6px;top:209px">
      <div class="office__label">CORPORATE OFFICE</div>
      <div class="office__phone">214-555-0147</div>
      <div class="office__address">207 West Birch Road, Loving, NM 88260</div>
    </div>

    <h2 class="abs pitch" style="left:309px;top:60px">Experienced Provider<br>To Oil, Gas, Energy &amp;<br>Construction Industries</h2>

    <ul class="abs features" style="left:309px;top:145px">
      <li><svg viewBox="0 0 22 12"><path d="M1 11 L20 2 M13 1.5 L20 2 L17 8" stroke="#8c181b" stroke-width="2" fill="none"/></svg>Consolidated Billing</li>
      <li><svg viewBox="0 0 22 12"><path d="M1 11 L20 2 M13 1.5 L20 2 L17 8" stroke="#8c181b" stroke-width="2" fill="none"/></svg>Full Service Corporate Lodging</li>
      <li><svg viewBox="0 0 22 12"><path d="M1 11 L20 2 M13 1.5 L20 2 L17 8" stroke="#8c181b" stroke-width="2" fill="none"/></svg>Live Customer Support 24/7/365</li>
      <li><svg viewBox="0 0 22 12"><path d="M1 11 L20 2 M13 1.5 L20 2 L17 8" stroke="#8c181b" stroke-width="2" fill="none"/></svg>Proven Track Record Of Performance</li>
      <li><svg viewBox="0 0 22 12"><path d="M1 11 L20 2 M13 1.5 L20 2 L17 8" stroke="#8c181b" stroke-width="2" fill="none"/></svg>Best Negotiated Rates &amp; No Additional Fees</li>
    </ul>

    <div class="card__band">www.SGPOilField.com</div>
  </section>

</main>
</body>
</html>
```